PROPERTY MANAGEMENT AND REAL ESTATE

Target Market(s)

real estate owners and investors

Industry/Entity Type

Real Estate

Contact Information for Business Card

BRIGHT HARBOR PROPERTY MANAGEMENT GROUP, LLC
287 West Marlow Parkway
Suite 240
Hallandale Beach, FL 33009

```html
<!DOCTYPE html>
<html lang="en">
<head>
<meta charset="utf-8">
<title>Bright Harbor Property Management Group – Business Card</title>
<link rel="stylesheet" href="https://fonts.googleapis.com/css2?family=Teko:wght@500&family=Exo+2:wght@300;400;500&display=swap">
<style>
  :root {
    --page: #b9b9b9;
    --card-white: #ffffff;
    --light: #eeeeee;
    --black: #1b1b1b;
    --stripe: #8d8d8d;
    --ink: #3a3a3a;
    --red: #8e1b1b;
    --chip: #c9c9c9;
  }
  * { box-sizing: border-box; margin: 0; padding: 0; }
  html, body { width: 1200px; height: 894px; overflow: hidden; }
  body {
    background: var(--page);
    font-family: "Exo 2", sans-serif;
    position: relative;
  }
  .card {
    position: absolute;
    width: 560px;
    height: 320px;
    box-shadow: 0 6px 18px rgba(0,0,0,0.25);
    overflow: hidden;
  }
  /* Front: name and contacts */
  .card-front { left: 70px; top: 480px; background: var(--black); }
  .band-light {
    position: absolute; left: 0; right: 0; top: 50px; height: 194px;
    background: linear-gradient(90deg, #e2e2e2, var(--light) 45%, #f6f6f6);
    border-top: 8px solid var(--stripe);
    border-bottom: 8px solid var(--stripe);
  }
  .band-dark-bottom {
    position: absolute; left: 0; right: 0; bottom: 0; height: 76px;
    background: linear-gradient(180deg, #111, #2a2a2a);
  }
  .identity { position: absolute; left: 30px; top: 82px; width: 280px; }
  .person-name {
    font-family: "Teko", sans-serif; font-weight: 500;
    font-size: 52px; line-height: 0.9; color: var(--ink); letter-spacing: 1px;
    white-space: nowrap;
  }
  .person-role {
    font-size: 12px; letter-spacing: 1px; color: #555;
    border-top: 2px solid #777; padding-top: 4px; margin-top: 4px; width: 168px;
  }
  .website {
    margin-top: 8px; display: inline-block; background: var(--chip);
    font-size: 10px; color: #444; padding: 4px 10px; letter-spacing: 0.5px;
  }
  .contacts { position: absolute; left: 330px; top: 112px; list-style: none; width: 220px; }
  .contacts li {
    display: flex; align-items: center; gap: 10px; margin-bottom: 12px;
    font-size: 12px; color: var(--ink); letter-spacing: 0.3px; line-height: 1.3;
    white-space: nowrap;
  }
  .contacts svg { flex: none; }
  /* Back: company name */
  .card-back { left: 570px; top: 90px; background: var(--card-white); }
  .brand {
    position: absolute; left: 110px; top: 122px;
    display: flex; align-items: center; gap: 18px;
  }
  .brand-dot { width: 62px; height: 62px; border-radius: 50%; background: var(--red); flex: none; }
  .brand-name {
    font-size: 17px; font-weight: 400; color: var(--black);
    letter-spacing: 0.5px; line-height: 1.3; text-transform: uppercase;
  }
</style>
</head>
<body>
  <section class="card card-back">
    <div class="brand">
      <span class="brand-dot"></span>
      <p class="brand-name">Bright Harbor Property<br>Management Group, LLC</p>
    </div>
  </section>

  <section class="card card-front">
    <div class="band-light"></div>
    <div class="band-dark-bottom"></div>
    <div class="identity">
      <h1 class="person-name">MARCUS HALE</h1>
      <p class="person-role">GENERAL MANAGER</p>
      <span class="website">www.brightharborpm.com</span>
    </div>
    <ul class="contacts">
      <li>
        <svg width="26" height="26" viewBox="0 0 28 28"><circle cx="14" cy="14" r="14" fill="#8e1b1b"/><path d="M14 6.5a5 5 0 0 0-5 5c0 3.8 5 9.5 5 9.5s5-5.7 5-9.5a5 5 0 0 0-5-5z" fill="#fff"/><circle cx="14" cy="11.5" r="2" fill="#8e1b1b"/></svg>
        <span>287 West Marlow Parkway<br>Suite 240</span>
      </li>
      <li>
        <svg width="26" height="26" viewBox="0 0 28 28"><circle cx="14" cy="14" r="14" fill="#8e1b1b"/><rect x="10" y="6.5" width="8" height="15" rx="1.5" fill="none" stroke="#fff" stroke-width="1.6"/><circle cx="14" cy="19" r="0.9" fill="#fff"/></svg>
        <span>305 555 0142</span>
      </li>
      <li>
        <svg width="26" height="26" viewBox="0 0 28 28"><circle cx="14" cy="14" r="14" fill="#8e1b1b"/><rect x="7.5" y="9.5" width="13" height="9" fill="#fff"/><path d="M7.5 9.5l6.5 5 6.5-5" fill="none" stroke="#8e1b1b" stroke-width="1.2"/></svg>
        <span>info@brightharborpm.com</span>
      </li>
    </ul>
  </section>
</body>
</html>
```